Flyer for Custom Home Builder!

my company is Harlow Ridge Homes, I am looking for a flyer that we can send via email to a customer, or print and hand out. I am thinking four pages so we could print this and fold it., possibly creating a folder. The name of the company is Harlow Ridge Homes our website is here www.harlowridgehomes-example.com. Some text you can use "Crafting luxury homes isn't just a job, it's our passion.
With meticulous attention to detail and an unwavering commitment to using the finest materials, Harlow Ridge Homes consistently delivers exceptional results that stand as a testament to our commitment to quality."

"Trust is the cornerstone of our foundation.
With a proven track record of delivering on our promises for over 16 years, we prioritize transparent communication and integrity throughout every step of the home-building journey".

you may need to obtain the photos here
https://files.example-share.net/f/k27pw4m8zrt03xq61bnv/h?key=48vn2c9q1x7mb5t0ekd3h&dl=0

Target Market(s)

We build homes for every wealthy clients, therefore the photos are extremely important

Industry/Entity Type

Construction.

Requirements
Must have
• clear larger photos

```html
<!DOCTYPE html>
<html lang="en">
<head>
<meta charset="utf-8">
<title>Harlow Ridge Homes — Flyer</title>
<link href="https://fonts.googleapis.com/css2?family=Montserrat:ital,wght@0,400;0,500;0,700;0,800;1,500;1,600;1,900&display=swap" rel="stylesheet">
<style>
  :root {
    --ring-blue: #1570c0;
    --sky-blue: #4aa9e2;
    --navy: #2d5a8b;
    --ink: #0d0d0d;
    --grey-brand: #4a4a4a;
    --paper: #ffffff;
  }
  * { margin: 0; padding: 0; box-sizing: border-box; }
  html, body { width: 920px; height: 1200px; overflow: hidden; background: var(--paper); }
  body { font-family: "Montserrat", Arial, sans-serif; color: var(--ink); }
  .flyer { position: relative; width: 920px; height: 1200px; overflow: hidden; background: var(--paper); }
  .shapes { position: absolute; inset: 0; }
  .brand {
    position: absolute; left: 560px; top: 66px; width: 320px;
    text-align: center; font-weight: 800; font-size: 30px; line-height: 1.15;
    letter-spacing: 1px; text-transform: uppercase; color: var(--grey-brand);
  }
  .headline { position: absolute; left: 50px; top: 356px; font-style: italic; text-transform: uppercase; white-space: nowrap; }
  .headline .line { display: block; }
  .headline .big { font-size: 57px; line-height: 58px; font-weight: 600; color: var(--sky-blue); }
  .headline .big b { font-weight: 900; color: var(--ink); }
  .headline .small { font-size: 21px; line-height: 38px; font-weight: 600; color: var(--ink); padding-top: 4px; }
  .intro {
    position: absolute; left: 50px; top: 578px; width: 820px;
    font-size: 13px; line-height: 1.4; text-align: justify; color: #1a1a1a;
  }
  .trust {
    position: absolute; left: 47px; top: 632px; font-style: italic; font-weight: 500;
    font-size: 33px; line-height: 1.12; text-transform: uppercase; color: var(--ink); white-space: nowrap;
  }
  .trust span { color: var(--sky-blue); }
  .track {
    position: absolute; left: 50px; top: 742px; width: 560px;
    font-size: 13px; line-height: 1.4; text-align: justify; color: #1a1a1a;
  }
  .contact { position: absolute; left: 0; top: 1030px; }
  .contact .cta { margin-left: 31px; font-size: 19px; font-weight: 800; color: var(--navy); }
  .contact .phone { margin-left: 30px; margin-top: 4px; font-size: 34px; font-weight: 700; color: var(--ink); letter-spacing: -0.5px; }
  .contact .email {
    display: inline-block; white-space: nowrap;
    margin-top: 8px; height: 32px; padding: 0 16px 0 31px;
    background: var(--navy); border-radius: 0 16px 16px 0;
    color: var(--paper); font-size: 15px; line-height: 32px;
  }
  .contact .address { margin: 10px 0 0 31px; font-size: 12px; line-height: 1.45; color: var(--ink); }
</style>
</head>
<body>
<div class="flyer">
  <svg class="shapes" width="920" height="1200" viewBox="0 0 920 1200">
    <defs>
      <linearGradient id="tinted" x1="0" y1="0" x2="1" y2="1">
        <stop offset="0" stop-color="#2a5f93"/>
        <stop offset="1" stop-color="#4c8fc0"/>
      </linearGradient>
      <linearGradient id="poolside" x1="0" y1="0" x2="0" y2="1">
        <stop offset="0" stop-color="#b7a58e"/>
        <stop offset="0.45" stop-color="#d8d6d0"/>
        <stop offset="1" stop-color="#6fb0c4"/>
      </linearGradient>
      <linearGradient id="dusk" x1="0" y1="0" x2="0" y2="1">
        <stop offset="0" stop-color="#8aa3bd"/>
        <stop offset="0.55" stop-color="#5f6b76"/>
        <stop offset="1" stop-color="#3c4a58"/>
      </linearGradient>
      <linearGradient id="interior" x1="0" y1="0" x2="0" y2="1">
        <stop offset="0" stop-color="#e9e8e4"/>
        <stop offset="1" stop-color="#b9a990"/>
      </linearGradient>
    </defs>

    <g role="img" aria-label="Blue-tinted photo of a modern home terrace with lounge seating and pool">
      <circle cx="700" cy="30" r="410" fill="url(#tinted)"/>
    </g>
    <circle cx="715" cy="58" r="212" fill="var(--paper)"/>

    <circle cx="190" cy="112" r="210" fill="var(--ring-blue)"/>
    <g role="img" aria-label="Photo of a luxury home patio with outdoor lounge and swimming pool">
      <circle cx="184" cy="104" r="202" fill="url(#poolside)"/>
    </g>

    <g role="img" aria-label="Blue-tinted photo of a bright open-plan living room with tall windows">
      <circle cx="262" cy="1160" r="365" fill="url(#tinted)"/>
    </g>
    <circle cx="140" cy="1232" r="268" fill="var(--paper)"/>

    <circle cx="766" cy="858" r="128" fill="var(--ring-blue)"/>
    <g role="img" aria-label="Photo of a modern home exterior with pool deck">
      <circle cx="762" cy="852" r="120" fill="url(#poolside)"/>
    </g>
    <circle cx="766" cy="1042" r="128" fill="var(--ring-blue)"/>
    <g role="img" aria-label="Photo of an open dining and living area with fireplace">
      <circle cx="762" cy="1048" r="120" fill="url(#interior)"/>
    </g>
    <circle cx="618" cy="962" r="96" fill="var(--ring-blue)"/>
    <g role="img" aria-label="Photo of a modern home at dusk reflected in an infinity pool">
      <circle cx="624" cy="962" r="88" fill="url(#dusk)"/>
    </g>
  </svg>

  <div class="brand">Harlow Ridge<br>Homes</div>

  <h1 class="headline">
    <span class="line big">Crafting</span>
    <span class="line big">Luxury <b>Homes</b></span>
    <span class="line small">Isn't just a job,</span>
    <span class="line big">It's our <b>Passion.</b></span>
  </h1>

  <p class="intro">With meticulous attention to detail and an unwavering commitment to using the finest materials, Harlow Ridge Homes consistently delivers exceptional results that stand as a testament to our commitment to quality."</p>

  <h2 class="trust">Trust is the <span>Cornerstone</span><br>of our foundation</h2>

  <p class="track">With a proven track record of delivering on our promises for over 16 years, we prioritize transparent communication and integrity throughout every step of the home-building journey</p>

  <div class="contact">
    <div class="cta">CALL NOW TODAY!</div>
    <div class="phone">555-014-2870</div>
    <div class="email">info@harlowridgehomes-example.com</div>
    <div class="address">480 Cedar Bluff Lane, Suite 200,<br>Fairview Tx 75000</div>
  </div>
</div>
</body>
</html>
```